BOLD & MINIMALIST DESIGN NEEDED

We want a very bold but minimalistic business card design that is impactful and utilizes both sides of the business card. Our current logo is included for your use.

We want bold fonts and good use of negative space. We don't want the logo to overpower the design.

Target Market(s)

Professionals who are building new commercial buildings.

Industry/Entity Type

Construction

Contact Information for Business Card

Name, Title, email, office phone, cell phone, website

Font styles to use
Serif
Sans Serif

Requirements
Must have
• Bold design!

```html
<!DOCTYPE html>
<html lang="en">
<head>
<meta charset="utf-8">
<title>Ridgeline Build – Business Card</title>
<link href="https://fonts.googleapis.com/css2?family=Montserrat:wght@400;500;800&display=swap" rel="stylesheet">
<style>
  :root {
    --stage: #3b3b3b;
    --card: #1d1d1d;
    --card-deep: #141414;
    --accent: #7cc242;
    --ink: #f2f2f2;
    --muted: #cfcfcf;
  }
  * { box-sizing: border-box; margin: 0; padding: 0; }
  html, body { width: 1200px; height: 791px; overflow: hidden; }
  body {
    background: var(--stage);
    font-family: "Montserrat", Arial, sans-serif;
    display: flex;
    align-items: center;
    justify-content: center;
    gap: 60px;
  }
  .card {
    width: 520px;
    height: 297px;
    background: var(--card);
    border: 2px solid var(--accent);
    position: relative;
    overflow: hidden;
  }
  /* Front side */
  .card-front { display: flex; align-items: center; }
  .brand-block {
    width: 250px;
    display: flex;
    align-items: center;
    justify-content: center;
    gap: 10px;
    padding-left: 20px;
  }
  .brand-mark {
    width: 14px; height: 14px;
    background: var(--accent);
  }
  .brand-name {
    font-weight: 800;
    font-size: 26px;
    letter-spacing: 0.5px;
    color: var(--ink);
    text-transform: uppercase;
  }
  .divider {
    width: 1px;
    height: 110px;
    background: var(--accent);
    margin: 0 26px 0 6px;
    align-self: flex-start;
    margin-top: 40px;
  }
  .contact-block { align-self: flex-start; margin-top: 36px; }
  .person-name {
    font-weight: 800;
    font-size: 19px;
    color: var(--accent);
    text-transform: uppercase;
    letter-spacing: 0.3px;
  }
  .person-title {
    font-size: 12px;
    color: var(--muted);
    margin-top: 2px;
  }
  .contact-list { list-style: none; margin-top: 22px; }
  .contact-list li {
    display: flex;
    align-items: center;
    gap: 8px;
    font-size: 11.5px;
    color: var(--ink);
    line-height: 20px;
  }
  .contact-list svg { width: 11px; height: 11px; flex: none; }
  /* Back side */
  .card-back { display: flex; align-items: center; justify-content: center; }
  .back-pattern {
    position: absolute; inset: 0;
    background: linear-gradient(135deg, var(--card-deep) 0%, #262626 55%, #343434 100%);
  }
  .back-brand {
    position: relative;
    display: flex;
    align-items: center;
    gap: 8px;
    margin-left: 180px;
    margin-top: 40px;
  }
  .back-brand .brand-name { font-size: 18px; }
  .back-brand .brand-mark { width: 10px; height: 10px; }
</style>
</head>
<body>
  <section class="card card-front">
    <div class="brand-block">
      <span class="brand-mark"></span>
      <span class="brand-name">Ridgeline Build</span>
    </div>
    <div class="divider"></div>
    <div class="contact-block">
      <p class="person-name">Marcus Reid</p>
      <p class="person-title">President</p>
      <ul class="contact-list">
        <li>
          <svg viewBox="0 0 12 12"><path d="M2 1h3l1 3-2 1a7 7 0 0 0 3 3l1-2 3 1v3c-6 0-9-3-9-9z" fill="var(--accent)"/></svg>
          555-204-1180
        </li>
        <li>
          <svg viewBox="0 0 12 12"><rect x="3" y="0.5" width="6" height="11" rx="1" fill="none" stroke="var(--ink)"/><circle cx="6" cy="9.5" r="0.7" fill="var(--ink)"/></svg>
          555-204-1180
        </li>
        <li>
          <svg viewBox="0 0 12 12"><rect x="0.5" y="2.5" width="11" height="7" fill="var(--accent)"/><path d="M0.5 2.5 6 7l5.5-4.5" fill="none" stroke="var(--card)"/></svg>
          m.reid@ridgeline-build.com
        </li>
        <li>
          <svg viewBox="0 0 12 12"><circle cx="6" cy="6" r="5.5" fill="var(--accent)"/><path d="M0.5 6h11M6 0.5c-3 3-3 8 0 11M6 0.5c3 3 3 8 0 11" fill="none" stroke="var(--card)" stroke-width="0.8"/></svg>
          www.ridgeline-build.com
        </li>
      </ul>
    </div>
  </section>

  <section class="card card-back">
    <div class="back-pattern" role="img" aria-label="Repeating tone-on-tone brand emblem pattern in dark grey gloss"></div>
    <div class="back-brand">
      <span class="brand-mark"></span>
      <span class="brand-name">Ridgeline Build</span>
    </div>
  </section>
</body>
</html>
```